Velor Stationery Design

We need Business Card, Letterhead, #10 Envelope , 3" x 4" Mailing Label, and email signature block. Also need "Aircraft Services" added small under the logo on everything except the email signature block. "Aircraft Services" should be in a simple font to to conflict with or distract from the logo. Our address info is:
4817 Marlow Bend NW
Kennesaw, GA 30144
P 555.284.6613
C 555.284.6613 (for biz cards only)
pete@velorjet.example (for biz cards only)
Website velorjet.example
Feel free to play around with colors but I expect that black or gray will work best for the address/phone info etc.

Target Market(s)

Aircraft owners

Industry/Entity Type

Aviation

Colors

Designer to choose only greyscale colors for use in the design.

Requirements
Must have
• Clean and sophisticated design -

```html
<!DOCTYPE html>
<html lang="en">
<head>
<meta charset="utf-8">
<title>Velor Business Card</title>
<link href="https://fonts.googleapis.com/css2?family=Open+Sans:wght@400;600;700&display=swap" rel="stylesheet">
<style>
  :root {
    --backdrop: #c4c3bf;
    --card-black: #1b1b1c;
    --accent-grey: #9c9c9c;
    --paper-white: #ffffff;
    --text-light: #f2f2f2;
    --text-muted: #bdbdbd;
    --text-dark: #2a2a2a;
    --pattern-grey: #2a2a2b;
  }
  * { margin: 0; padding: 0; box-sizing: border-box; }
  html, body { width: 1200px; height: 857px; overflow: hidden; }
  body {
    background: var(--backdrop);
    font-family: "Open Sans", Arial, sans-serif;
    position: relative;
  }
  .card {
    position: absolute;
    width: 520px;
    height: 297px;
    background: var(--card-black);
    border-bottom: 3px solid var(--accent-grey);
    overflow: hidden;
    box-shadow: 0 14px 30px rgba(0,0,0,0.28);
  }
  .card-front { left: 60px; top: 150px; }
  .card-back { left: 620px; top: 410px; }

  .front-swoosh { position: absolute; inset: 0; }

  .brand { position: absolute; left: 44px; top: 62px; }
  .wordmark {
    font-weight: 700;
    font-size: 46px;
    letter-spacing: 4px;
    color: var(--accent-grey);
    line-height: 1;
  }
  .tagline {
    margin-top: 6px;
    padding-left: 2px;
    font-size: 9px;
    font-weight: 400;
    letter-spacing: 3.2px;
    color: var(--text-muted);
    text-transform: uppercase;
  }
  .address {
    position: absolute;
    left: 46px;
    top: 148px;
    font-style: normal;
    color: var(--text-light);
    font-size: 12.5px;
    line-height: 1.45;
  }
  .contact-list {
    position: absolute;
    left: 46px;
    top: 196px;
    list-style: none;
    color: var(--text-light);
    font-size: 12.5px;
    line-height: 1.45;
  }
  .contact-list li { display: flex; align-items: center; gap: 8px; }
  .contact-list svg { width: 10px; height: 10px; fill: var(--accent-grey); flex: none; }

  .person {
    position: absolute;
    left: 232px;
    top: 58px;
    padding-left: 12px;
    border-left: 2px solid var(--accent-grey);
    white-space: nowrap;
  }
  .person-name {
    color: var(--accent-grey);
    font-size: 15px;
    font-weight: 400;
    letter-spacing: 0.3px;
  }
  .person-title {
    color: var(--text-light);
    font-size: 10.5px;
  }

  .website {
    position: absolute;
    right: 24px;
    bottom: 26px;
    font-size: 12px;
    letter-spacing: 3px;
    color: var(--text-dark);
  }
  .website .domain { color: #6e6e6e; font-weight: 600; }

  .back-pattern { position: absolute; inset: 0; }
  .back-wordmark {
    position: absolute;
    left: 50%;
    top: 50%;
    transform: translate(-50%, -50%);
    font-weight: 700;
    font-size: 34px;
    letter-spacing: 3px;
    color: var(--accent-grey);
    line-height: 1;
  }
</style>
</head>
<body>

  <section class="card card-front">
    <svg class="front-swoosh" viewBox="0 0 520 297" preserveAspectRatio="none" aria-hidden="true">
      <path d="M520 36 L520 297 L282 297 C300 230 390 150 520 36 Z" fill="var(--accent-grey)"/>
      <path d="M520 50 L520 297 L298 297 C318 238 404 162 520 50 Z" fill="var(--paper-white)"/>
    </svg>

    <div class="brand">
      <div class="wordmark">VELOR</div>
      <div class="tagline">Aircraft Services</div>
    </div>

    <address class="address">
      4817 Marlow Bend NW<br>
      Kennesaw, GA 30144
    </address>

    <ul class="contact-list">
      <li><svg viewBox="0 0 10 10"><path d="M2 0.5 L4 3 L3 4 C3.6 5.4 4.6 6.4 6 7 L7 6 L9.5 8 L8.4 9.5 C4.5 9.2 0.8 5.5 0.5 1.6 Z"/></svg>555.284.6613</li>
      <li><svg viewBox="0 0 10 10"><path d="M2.5 0 H7.5 V10 H2.5 Z M3.4 1 V8 H6.6 V1 Z"/></svg>555.284.6613</li>
      <li><svg viewBox="0 0 10 10"><path d="M0 2 H10 V8.5 H0 Z M0.8 2.6 L5 5.6 L9.2 2.6 Z"/></svg>pete@velorjet.example</li>
    </ul>

    <div class="person">
      <div class="person-name">DANIEL CORWIN</div>
      <div class="person-title">Development Manager Officer</div>
    </div>

    <div class="website">www.<span class="domain">velorjet</span>.example</div>
  </section>

  <section class="card card-back">
    <svg class="back-pattern" viewBox="0 0 520 297" preserveAspectRatio="none" role="img" aria-label="Repeating gloss brand-name pattern across the card back">
      <defs>
        <linearGradient id="glossFade" x1="0" y1="1" x2="1" y2="0">
          <stop offset="0" stop-color="#111" stop-opacity="0.6"/>
          <stop offset="1" stop-color="#2a2a2b" stop-opacity="0.9"/>
        </linearGradient>
      </defs>
      <rect width="520" height="297" fill="var(--card-black)"/>
      <rect width="520" height="297" fill="url(#glossFade)"/>
    </svg>
    <div class="back-wordmark">VELOR</div>
  </section>

</body>
</html>
```